Birch Flooring Supply

Basic one-sided business card design using the attached logo. Vintage americana theme. Font is modified Arial Nova Cond, but anything that coordinates can be used

```html
<!DOCTYPE html>
<html lang="en">
<head>
<meta charset="UTF-8">
<title>Birch Flooring Supply – Business Card</title>
<link rel="stylesheet" href="https://fonts.googleapis.com/css2?family=Arimo:wght@400;700&display=swap">
<style>
  :root {
    --stage: #2a2a2b;
    --tan: #b09270;
    --charcoal: #333333;
    --paper: #f8f8f8;
    --ink: #2b2b2b;
  }
  * { box-sizing: border-box; margin: 0; padding: 0; }
  html, body { width: 1200px; height: 840px; overflow: hidden; }
  body {
    background: var(--stage);
    font-family: "Arimo", Arial, sans-serif;
    display: flex;
    flex-direction: column;
    align-items: center;
    justify-content: center;
    gap: 44px;
  }
  .card {
    position: relative;
    width: 620px;
    height: 354px;
    border-radius: 26px;
    overflow: hidden;
  }
  .card-back {
    background: var(--tan);
    display: flex;
    align-items: center;
    justify-content: center;
  }
  .brand-name {
    font-family: "Arimo", Arial, sans-serif;
    font-weight: 700;
    text-transform: uppercase;
    text-align: center;
    letter-spacing: 0.04em;
    line-height: 1.15;
  }
  .card-back .brand-name { color: var(--charcoal); font-size: 34px; }
  .card-front {
    background: var(--paper);
    border-bottom: 5px solid var(--tan);
  }
  .front-disc { position: absolute; inset: 0; width: 100%; height: 100%; }
  .card-front .brand-name {
    position: absolute;
    left: 356px;
    top: 104px;
    width: 220px;
    color: var(--paper);
    font-size: 28px;
  }
  .holder { position: absolute; left: 46px; top: 150px; }
  .holder-name {
    color: var(--tan);
    font-weight: 700;
    font-size: 21px;
    letter-spacing: 0.02em;
    text-transform: uppercase;
  }
  .holder-role { color: var(--ink); font-size: 15px; margin-top: 2px; }
  .address {
    position: absolute;
    left: 46px;
    top: 218px;
    color: var(--ink);
    font-size: 15px;
    line-height: 1.25;
  }
  .contact-list {
    position: absolute;
    left: 46px;
    top: 270px;
    list-style: none;
    color: var(--ink);
    font-size: 15px;
  }
  .contact-list li { display: flex; align-items: center; gap: 9px; height: 21px; }
  .contact-list svg { width: 13px; height: 13px; flex: none; }
</style>
</head>
<body>

  <section class="card card-back">
    <p class="brand-name">Birch<br>Flooring Supply</p>
  </section>

  <section class="card card-front">
    <svg class="front-disc" viewBox="0 0 620 354" aria-hidden="true">
      <circle cx="468" cy="140" r="226" fill="var(--charcoal)"/>
      <circle cx="468" cy="140" r="210" fill="none" stroke="var(--tan)" stroke-width="3"/>
    </svg>
    <p class="brand-name">Birch<br>Flooring Supply</p>

    <div class="holder">
      <p class="holder-name">Daniel Carter</p>
      <p class="holder-role">Manager</p>
    </div>

    <p class="address">Your Address, City<br>State, Zip 0000</p>

    <ul class="contact-list">
      <li>
        <svg viewBox="0 0 16 16"><path d="M4 1.5 6.2 4 5 5.6c.8 1.9 2.4 3.5 4.3 4.3L11 8.7l2.5 2.2-1.2 2.5C7 13.6 2.4 9 2.6 3.6Z" fill="none" stroke="var(--tan)" stroke-width="1.5" stroke-linejoin="round"/></svg>
        123-456-2100
      </li>
      <li>
        <svg viewBox="0 0 16 16"><rect x="1.5" y="3.5" width="13" height="9" fill="none" stroke="var(--tan)" stroke-width="1.4"/><path d="M1.5 3.5 8 9l6.5-5.5" fill="none" stroke="var(--tan)" stroke-width="1.4"/></svg>
        youremail@birchmail.com
      </li>
      <li>
        <svg viewBox="0 0 16 16"><circle cx="8" cy="8" r="6.5" fill="none" stroke="var(--tan)" stroke-width="1.3"/><ellipse cx="8" cy="8" rx="2.8" ry="6.5" fill="none" stroke="var(--tan)" stroke-width="1.1"/><path d="M1.5 8h13M2.6 4.8h10.8M2.6 11.2h10.8" stroke="var(--tan)" stroke-width="1.1"/></svg>
        www.yourwebsite.com
      </li>
    </ul>
  </section>

</body>
</html>
```